Podcast cover design for a new podcast called 'Formosan Trail Blazers'

I would like a clean, professional and impactful design for a new podcast I am launching called 'Formosan Trail Blazers'. 'Formosan Trail Blazers,' is a podcast featuring conversations with the island's groundbreaking entrepreneurs, technologists, artists, and scientists. Each episode uncovers the stories and insights of visionaries who are shaping Taiwan's future through cutting-edge startups, technological breakthroughs, artistic innovation, and scientific discovery. The podcast cover needs to look professional and be impactful. Ideally, I would also like the podcast cover to feature an photo or image of myself. Please see uploaded two recent photos of myself which you can crop etc for the podcast cover.

```html
<!DOCTYPE html>
<html lang="en">
<head>
<meta charset="utf-8">
<title>Formosan Trail Blazers – Podcast Cover</title>
<link rel="stylesheet" href="https://fonts.googleapis.com/css2?family=Bebas+Neue&family=Poppins:wght@500;600&display=swap">
<style>
  :root {
    --stage: #e4e4e4;
    --cover-black: #050505;
    --foliage: #1c2a18;
    --hair: #5a3a22;
    --skin: #c08a6c;
    --skin-shade: #8d5f48;
    --shirt: #d9d9d6;
    --blazer: #1b1b1b;
    --lime: #a3b93a;
    --white: #ffffff;
    --ink: #0a0a0a;
  }
  * { box-sizing: border-box; margin: 0; padding: 0; }
  html, body {
    width: 1200px;
    height: 807px;
    overflow: hidden;
    background: var(--stage);
  }
  .stage {
    position: relative;
    width: 1200px;
    height: 807px;
  }
  .podcast-cover {
    position: absolute;
    left: 220px;
    top: 23px;
    width: 760px;
    height: 760px;
    overflow: hidden;
    background:
      radial-gradient(ellipse 60% 35% at 55% 8%, var(--foliage) 0%, rgba(28,42,24,0) 70%),
      var(--cover-black);
  }
  .host-photo {
    position: absolute;
    left: 36px;
    top: 30px;
    width: 430px;
    height: 730px;
    border-radius: 215px 215px 0 0;
    background: linear-gradient(180deg,
      var(--hair) 0%,
      var(--skin-shade) 14%,
      var(--skin) 30%,
      var(--skin-shade) 50%,
      var(--shirt) 62%,
      var(--blazer) 78%,
      var(--cover-black) 100%);
    -webkit-mask-image: linear-gradient(90deg, rgba(0,0,0,0.85) 0%, #000 20%, #000 80%, rgba(0,0,0,0.85) 100%);
            mask-image: linear-gradient(90deg, rgba(0,0,0,0.85) 0%, #000 20%, #000 80%, rgba(0,0,0,0.85) 100%);
  }
  .island-outline {
    position: absolute;
    left: 430px;
    top: 135px;
    width: 280px;
    height: 480px;
    background: radial-gradient(ellipse 35% 48% at 50% 50%, rgba(90,90,90,0.18) 0%, rgba(90,90,90,0) 75%);
  }
  .show-title {
    position: absolute;
    right: 27px;
    top: 233px;
    text-align: right;
    font-family: "Bebas Neue", sans-serif;
    font-weight: 400;
    line-height: 0.8;
    letter-spacing: 0.5px;
  }
  .show-title__lead {
    display: block;
    color: var(--white);
    font-size: 86px;
    margin-bottom: 1px;
  }
  .show-title__main {
    display: block;
    color: var(--lime);
    font-size: 142px;
    margin-bottom: 8px;
  }
  .host-credit {
    position: absolute;
    right: 27px;
    top: 533px;
    width: 266px;
    height: 142px;
    border-right: 2px solid var(--lime);
  }
  .host-credit__with {
    position: absolute;
    right: 12px;
    top: 62px;
    font-family: "Poppins", sans-serif;
    font-weight: 500;
    font-size: 29px;
    line-height: 1;
    color: var(--white);
  }
  .host-credit__name {
    position: absolute;
    right: 0;
    top: 97px;
    width: 266px;
    height: 45px;
    border-radius: 6px 0 0 6px;
    background: var(--lime);
    color: var(--ink);
    font-family: "Poppins", sans-serif;
    font-weight: 600;
    font-size: 29px;
    line-height: 49px;
    text-align: right;
    padding-right: 11px;
  }
</style>
</head>
<body>
  <main class="stage">
    <section class="podcast-cover">
      <div class="island-outline" role="img" aria-label="Faint outline map of the island of Taiwan"></div>
      <div class="host-photo" role="img" aria-label="Head-and-shoulders portrait photo of the podcast host smiling, in a dark blazer and white open-collar shirt"></div>
      <h1 class="show-title">
        <span class="show-title__lead">Formosan</span>
        <span class="show-title__main">Trail</span>
        <span class="show-title__main">Blazers</span>
      </h1>
      <div class="host-credit">
        <p class="host-credit__with">WITH</p>
        <p class="host-credit__name">LOREM IPSUM</p>
      </div>
    </section>
  </main>
</body>
</html>
```